Home Security Company Business Card

Looking for a eye catching business card that is non traditional and stands out but yet still looks professional. It should include all the pertinent information such as name, title, address, telephone, e-mail, website address should definitely stand out and then finally the logo.

Target Market(s)

Residential and Commercial accounts mostly upscale accounts

Industry/Entity Type

Security

Contact Information for Business Card

Name
Title
Address
Office #
Cell #
E-mail
Website

Font styles to use
Serif
Sans Serif

Requirements
Must have
• Logo, two sided color configuration
Nice to have
• You decide
Should not have
• There really aren't any.

```html
<!DOCTYPE html>
<html lang="en">
<head>
<meta charset="utf-8">
<title>Ironvale Security Systems Inc. – Identity Presentation</title>
<link rel="stylesheet" href="https://fonts.googleapis.com/css2?family=Tinos:wght@400;700&family=Questrial&family=Arimo:wght@400;700&display=swap">
<style>
  :root {
    --maroon: #7a1008;
    --maroon-deep: #6e0d06;
    --gold: #d89a42;
    --gold-light: #fdf5dc;
    --amber-text: #d8922e;
    --grey-text: #7a7a7a;
    --label-grey: #4a4a4a;
    --navy: #1f2f5a;
    --white: #ffffff;
    --bg-light: #f2f2f2;
    --bg-dark: #8f8f8f;
  }
  * { margin: 0; padding: 0; box-sizing: border-box; }
  html, body { width: 979px; height: 1200px; overflow: hidden; }
  body { position: relative; background: var(--white); font-family: "Questrial", "Century Gothic", sans-serif; }

  .brand-dot { position: absolute; border-radius: 50%; background: var(--gold); }
  .card-back .brand-dot { background: var(--maroon); }

  .brand-hero { position: absolute; left: 0; top: 0; width: 979px; height: 490px; background: var(--white); }
  .brand-hero .brand-dot { left: 394px; top: 120px; width: 190px; height: 190px; }
  .wordmark { font-family: "Tinos", "Times New Roman", serif; font-weight: 400; color: var(--maroon); text-align: center; line-height: 1; }
  .brand-hero .wordmark { position: absolute; left: 0; width: 100%; top: 352px; }
  .wordmark .name { display: block; font-size: 42px; letter-spacing: 0.5px; }
  .wordmark .tagline { display: block; font-size: 19px; margin-top: 1px; }

  .gold-band { position: absolute; left: 0; top: 490px; width: 979px; height: 15px; background: var(--gold); }

  .showcase {
    position: absolute; left: 0; top: 505px; width: 979px; height: 678px;
    background: radial-gradient(ellipse 60% 55% at 50% 42%, var(--bg-light) 0%, #d4d4d4 55%, var(--bg-dark) 100%);
  }
  .section-label { position: absolute; font-family: "Arimo", Arial, sans-serif; font-weight: 700; font-size: 17px; color: var(--label-grey); text-align: center; }

  .card { position: absolute; width: 409px; height: 238px; box-shadow: 0 0 3px rgba(0,0,0,0.25); }
  .card-front { left: 61px; top: 80px; background: var(--white); }
  .card-back { left: 518px; top: 80px; background: linear-gradient(to bottom, var(--gold) 0%, #e9c58a 45%, var(--gold-light) 100%); }

  .card-front .brand-dot { left: 55px; top: 58px; width: 90px; height: 90px; }
  .card-back .brand-dot { left: 159px; top: 56px; width: 90px; height: 90px; }

  .card-front .wordmark { position: absolute; left: 20px; width: 160px; top: 167px; }
  .card .wordmark .name { font-size: 19px; }
  .card .wordmark .tagline { font-size: 8.5px; margin-top: 0; }
  .card-front .divider { position: absolute; left: 190px; top: 27px; width: 2px; height: 191px; background: #8a8a8a; }
  .card-back .wordmark { position: absolute; left: 0; width: 100%; top: 165px; }

  .contact { position: absolute; left: 215px; top: 44px; color: var(--grey-text); font-size: 10.5px; line-height: 13px; }
  .contact .person-name { font-size: 19px; color: var(--maroon); line-height: 22px; font-weight: 700; }
  .contact .person-title { font-size: 10.5px; }
  .contact .person-phone { color: var(--maroon); margin-top: 5px; }
  .contact .address { margin-top: 15px; }
  .contact .lines { margin-top: 15px; }
  .contact .lines b { color: var(--maroon); font-family: "Arimo", sans-serif; font-weight: 700; }

  .signature { position: absolute; left: 204px; top: 443px; width: 540px; height: 174px; background: var(--white); }
  .signature .brand-dot { left: 37px; top: 20px; width: 52px; height: 52px; }
  .signature .wordmark { position: absolute; left: 17px; width: 92px; top: 85px; }
  .signature .wordmark .name { font-size: 11px; }
  .signature .wordmark .tagline { font-size: 5px; }
  .sig-person { position: absolute; right: 124px; top: 34px; text-align: right; }
  .sig-person .person-name { font-size: 19px; color: var(--amber-text); font-weight: 700; line-height: 22px; }
  .sig-person .person-title { font-size: 11px; color: var(--maroon); }
  .sig-person .person-phone { font-size: 19px; color: var(--amber-text); font-weight: 700; margin-top: 2px; }
  .sig-photo { position: absolute; left: 424px; top: 9px; width: 72px; height: 102px; background: linear-gradient(to bottom, #e9eef7 0%, #b9cbe6 55%, #8fa8d0 100%); }
  .sig-bar { position: absolute; left: 10px; top: 111px; width: 521px; height: 18px; background: var(--maroon); }
  .sig-contact { position: absolute; left: 32px; top: 137px; font-family: "Arimo", sans-serif; font-size: 11.5px; color: var(--navy); line-height: 14px; }
  .sig-contact b { margin-right: 2px; }
  .sig-contact .gap { display: inline-block; width: 14px; }
  .web-button { position: absolute; left: 368px; top: 140px; width: 144px; height: 18px; background: linear-gradient(to bottom, #fbe6b8, var(--gold)); font-family: "Arimo", sans-serif; font-weight: 700; font-size: 9.5px; color: var(--maroon-deep); text-align: center; line-height: 18px; }

  .note { position: absolute; left: 0; width: 100%; top: 650px; text-align: center; font-family: "Arimo", Arial, sans-serif; font-weight: 700; font-size: 16px; color: var(--navy); }
  .footer-band { position: absolute; left: 0; top: 1183px; width: 979px; height: 17px; background: var(--maroon); }
</style>
</head>
<body>
  <header class="brand-hero">
    <div class="brand-dot"></div>
    <div class="wordmark">
      <span class="name">IRONVALE</span>
      <span class="tagline">SECURITY SYSTEMS INC.</span>
    </div>
  </header>

  <div class="gold-band"></div>

  <main class="showcase">
    <h2 class="section-label" style="left:61px; width:409px; top:48px;">Business Card Front:</h2>
    <h2 class="section-label" style="left:518px; width:409px; top:48px;">Business Card back:</h2>

    <section class="card card-front">
      <div class="brand-dot"></div>
      <div class="wordmark">
        <span class="name">IRONVALE</span>
        <span class="tagline">SECURITY SYSTEMS INC.</span>
      </div>
      <div class="divider"></div>
      <div class="contact">
        <div class="person-name">First Mid Last</div>
        <div class="person-title">Managing Director</div>
        <div class="person-phone">123-4567-890</div>
        <div class="address">Office No.123, ABC Building,<br>1st Floor, City, Country.</div>
        <div class="lines">
          <b>O:</b> 123-4567-890<br>
          <b>F:</b> 123-4567-890<br>
          <b>E:</b> info@yourdomain.com<br>
          <b>W:</b> www.yourdomain.com
        </div>
      </div>
    </section>

    <section class="card card-back">
      <div class="brand-dot"></div>
      <div class="wordmark">
        <span class="name">IRONVALE</span>
        <span class="tagline">SECURITY SYSTEMS INC.</span>
      </div>
    </section>

    <h2 class="section-label" style="left:204px; width:540px; top:415px;">Email Signature:</h2>

    <section class="signature">
      <div class="brand-dot"></div>
      <div class="wordmark">
        <span class="name">IRONVALE</span>
        <span class="tagline">SECURITY SYSTEMS INC.</span>
      </div>
      <div class="sig-person">
        <div class="person-name">First Mid Last</div>
        <div class="person-title">Managing Director</div>
        <div class="person-phone">123-4567-890</div>
      </div>
      <div class="sig-photo" role="img" aria-label="Portrait photo of the managing director"></div>
      <div class="sig-bar"></div>
      <div class="sig-contact">
        <b>Ph:</b> 123-4567-890<span class="gap"></span><b>Fax:</b> 123-4567-890<br>
        Office No.123, Abc Building, Ist Floor, City, Country
      </div>
      <div class="web-button">Click Here To Visit Our Web</div>
    </section>

    <p class="note">NOTE: FREE EMAIL SIGNATURE WILL BE PROVIDED (If the design will be selected as a winner)</p>
  </main>

  <div class="footer-band"></div>
</body>
</html>
```